Commercial painting contractor in need of graphic designs for new trade show booth.

Brellow Holdings, Inc. is a leading commercial and multifamily painter in Texas for new construction interested in growing its repaint business. We will be attending the Lone Pecan Rental Housing Guild Expo in October and are looking to finalize our booth design and get it ordered by 8/15. The booth layout is selected, and we have a logo and basic brand board. We are looking for graphic design that we can use for the next 3+ years without appearing dated. We are considering incorporating more of the baby blue color into our repaint branding (see bh-logo-dark blued-bg attached). The blue and white logo is our standard.
BrellowCo website: www.coatworksvale.com
Trade Show booth website: https://quickexhibitframes.com/10X10-Custom-Trade-Show-Display-Booth-I

```html
<!DOCTYPE html>
<html lang="en">
<head>
<meta charset="utf-8">
<title>Brellow Holdings, Inc. – Trade Show Booth Graphics</title>
<link rel="stylesheet" href="https://fonts.googleapis.com/css2?family=Arimo:wght@700&family=Raleway:wght@400;600;700&family=Tinos:ital@1&display=swap">
<style>
  :root {
    --royal: #2434c4;
    --royal-deep: #141c86;
    --navy: #1a2290;
    --lavender: #dfe2fb;
    --lavender-mid: #c9cdf2;
    --white: #ffffff;
    --band: #eeeff2;
    --ink: #1b1b24;
    --canvas: #f4f5f8;
  }
  * { box-sizing: border-box; margin: 0; padding: 0; }
  html, body { width: 1200px; height: 1200px; overflow: hidden; background: var(--canvas); }
  body { position: relative; font-family: "Raleway", sans-serif; }

  /* Back wall */
  .backwall {
    position: absolute; left: 40px; top: 30px; width: 1120px; height: 560px;
    border-radius: 24px 24px 0 0; overflow: hidden; background: var(--band);
  }
  .backwall-photo {
    position: absolute; left: 0; top: 0; width: 100%; height: 440px;
    background:
      radial-gradient(ellipse at 70% 30%, rgba(120,140,230,.55), transparent 60%),
      linear-gradient(180deg, #2d45c2 0%, #25399f 55%, #1c2a80 100%);
  }
  .backwall-message {
    position: absolute; left: 520px; top: 50px; width: 560px; text-align: center; color: var(--white);
  }
  .brand-name {
    display: inline-flex; align-items: center; gap: 10px;
    font-family: "Arimo", sans-serif; font-weight: 700; letter-spacing: .02em; text-transform: uppercase;
  }
  .brand-dot { width: 14px; height: 14px; border-radius: 50%; background: currentColor; }
  .brand-since { font-family: "Tinos", serif; font-style: italic; }
  .backwall-message .brand-name { font-size: 26px; }
  .backwall-message .brand-since { font-size: 20px; margin-top: 6px; }
  .headline { margin-top: 90px; font-weight: 700; font-size: 44px; line-height: 1.22; }
  .headline-since { font-weight: 400; font-size: 34px; margin-top: 10px; }
  .backwall-contact {
    position: absolute; left: 0; top: 440px; width: 100%; height: 120px;
    display: flex; flex-direction: column; align-items: center; justify-content: center; gap: 10px;
    padding-left: 420px; color: var(--ink);
  }
  .contact-phone { display: flex; align-items: center; gap: 12px; font-weight: 700; font-size: 34px; }
  .contact-web { font-weight: 700; font-size: 24px; letter-spacing: .12em; }

  /* Tower */
  .tower { position: absolute; left: 120px; top: 620px; width: 250px; height: 550px; }
  .tower svg { display: block; }

  /* Kiosk */
  .kiosk { position: absolute; left: 450px; top: 640px; width: 210px; height: 530px; }

  /* Counter */
  .counter {
    position: absolute; left: 700px; top: 770px; width: 460px; height: 400px;
    border-radius: 6px; overflow: hidden; background: var(--white);
    box-shadow: 0 0 0 1px #dcdde3;
  }
  .counter-face {
    height: 310px; background: linear-gradient(180deg, var(--royal) 0%, var(--royal-deep) 100%);
    color: var(--white); text-align: center; padding-top: 100px;
  }
  .counter-face .brand-name { font-size: 20px; }
  .counter-since { font-size: 30px; margin-top: 40px; }
  .counter-web {
    height: 90px; display: flex; align-items: center; justify-content: center;
    font-weight: 700; font-size: 22px; color: var(--ink); letter-spacing: .02em;
  }
</style>
</head>
<body>

  <section class="backwall">
    <div class="backwall-photo" role="img" aria-label="Photo of a tall apartment building framed by trees, tinted in royal blue"></div>
    <div class="backwall-message">
      <div class="brand-name"><span class="brand-dot"></span>Brellow Holdings, Inc.</div>
      <div class="brand-since">Since&nbsp; 1972</div>
      <h1 class="headline">Quality Painting<br>Within Texas &amp; Beyond</h1>
      <p class="headline-since">Since 1972</p>
    </div>
    <div class="backwall-contact">
      <div class="contact-phone">
        <svg width="34" height="34" viewBox="0 0 24 24" aria-hidden="true">
          <path fill="#1a2290" d="M6.6 10.8a15.1 15.1 0 0 0 6.6 6.6l2.2-2.2a1 1 0 0 1 1-.25 11.4 11.4 0 0 0 3.6.57 1 1 0 0 1 1 1V20a1 1 0 0 1-1 1A17 17 0 0 1 3 4a1 1 0 0 1 1-1h3.5a1 1 0 0 1 1 1c0 1.25.2 2.45.57 3.57a1 1 0 0 1-.25 1z"/>
          <path fill="none" stroke="#1a2290" stroke-width="1.8" stroke-linecap="round" d="M14.5 3.5a6 6 0 0 1 6 6M14.5 7a2.6 2.6 0 0 1 2.6 2.6"/>
        </svg>
        512-555-0148
      </div>
      <div class="contact-web">www.coatworksvale.com</div>
    </div>
  </section>

  <section class="tower">
    <svg width="250" height="550" viewBox="0 0 250 550">
      <defs>
        <linearGradient id="towerFill" x1="0" y1="0" x2="0" y2="1">
          <stop offset="0" stop-color="#e4e6fc"/>
          <stop offset="1" stop-color="#c9cdf2"/>
        </linearGradient>
      </defs>
      <path fill="url(#towerFill)" d="M10 90 Q10 10 125 4 Q240 10 240 90 Q240 130 220 160 Q200 190 200 240 L200 550 L50 550 L50 240 Q50 190 30 160 Q10 130 10 90 Z"/>
      <text x="125" y="100" text-anchor="middle" font-family="Arimo, sans-serif" font-weight="700" font-size="14" fill="#1a2290">BRELLOW HOLDINGS, INC.</text>
      <text x="125" y="122" text-anchor="middle" font-family="Tinos, serif" font-style="italic" font-size="13" fill="#1a2290">Since  1972</text>
      <circle cx="125" cy="60" r="9" fill="#1a2290"/>
      <text x="125" y="420" text-anchor="middle" font-family="Arimo, sans-serif" font-weight="700" font-size="12" fill="#1a2290">BRELLOW HOLDINGS, INC.</text>
    </svg>
  </section>

  <section class="kiosk">
    <svg width="210" height="530" viewBox="0 0 210 530">
      <defs>
        <linearGradient id="kioskFill" x1="0" y1="0" x2="0" y2="1">
          <stop offset="0" stop-color="#2434c4"/>
          <stop offset="1" stop-color="#141c86"/>
        </linearGradient>
        <clipPath id="kioskShape">
          <path d="M10 30 Q10 4 40 4 L170 4 Q200 4 200 30 L200 150 Q200 220 178 300 Q168 360 178 420 L205 530 L5 530 L32 420 Q42 360 32 300 Q10 220 10 150 Z"/>
        </clipPath>
      </defs>
      <g clip-path="url(#kioskShape)">
        <rect width="210" height="450" fill="url(#kioskFill)"/>
        <rect y="450" width="210" height="80" fill="#ffffff"/>
      </g>
      <text x="105" y="26" text-anchor="middle" font-family="Arimo, sans-serif" font-weight="700" font-size="8" fill="#ffffff">BRELLOW HOLDINGS, INC.</text>
      <text x="105" y="38" text-anchor="middle" font-family="Tinos, serif" font-style="italic" font-size="7" fill="#ffffff">Since 1972</text>
      <text x="105" y="260" text-anchor="middle" font-family="Raleway, sans-serif" font-size="30" fill="#ffffff">Since</text>
      <text x="105" y="296" text-anchor="middle" font-family="Raleway, sans-serif" font-size="30" fill="#ffffff">1972</text>
      <text x="105" y="497" text-anchor="middle" font-family="Raleway, sans-serif" font-weight="700" font-size="17" fill="#1b1b24">512-555-0148</text>
    </svg>
  </section>

  <section class="counter">
    <div class="counter-face">
      <div class="brand-name"><span class="brand-dot"></span>Brellow Holdings, Inc.</div>
      <p class="counter-since">Since 1972</p>
    </div>
    <div class="counter-web">www.coatworksvale.com</div>
  </section>

</body>
</html>
```